We need an attractive business card design that is modern and inviting. We like the blue and yellow (or gold) colors that are displayed with the logo. The business should communicate trust, experience, and integrity.

Target Market(s)

Residential and Commercial

Industry/Entity Type

Business

Contact Information for Business Card

Recessed Lighting
LED Retro Fit
Sign Repair
Alarms and Cameras
Mobile Home Services
24hr service calls

Font styles to use
Serif
Sans Serif

Colors
3176b5
0455a3
fece3e
fbee3e

Requirements
Must have
• Brondle Electric
• Owner: Marcus Tivane
• Licensed and Insured
• TECL #58917
Nice to have
• Exquisite Detail!!
• Over 20 years of experience
Should not have
• Nothing boring or traditional!!!

```html
<!DOCTYPE html>
<html lang="en">
<head>
<meta charset="utf-8">
<title>Brondle Electric – Business Card</title>
<link href="https://fonts.googleapis.com/css2?family=Roboto:wght@400;500;700&display=swap" rel="stylesheet">
<style>
  :root {
    --navy: #1c3b85;
    --yellow: #dbe000;
    --card: #f7f7f7;
    --ink: #2b2b2b;
    --backdrop: #e4e4e4;
    --ghost: rgba(28, 59, 133, 0.05);
  }
  * { box-sizing: border-box; margin: 0; padding: 0; }
  html, body {
    width: 1200px; height: 576px; overflow: hidden;
    background: var(--backdrop);
    font-family: "Roboto", sans-serif;
  }
  .canvas { position: relative; width: 1200px; height: 576px; }
  .card {
    position: absolute; top: 138px;
    width: 486px; height: 294px;
    background: var(--card);
    border-radius: 8px; overflow: hidden;
  }
  .card--front { left: 80px; }
  .card--back { left: 602px; }

  /* Front */
  .front-mark {
    position: absolute; left: 204px; top: 94px;
    width: 76px; height: 76px; border-radius: 50%;
    border: 6px solid var(--navy);
  }
  .front-name {
    position: absolute; left: 0; right: 0; top: 168px;
    text-align: center; font-size: 31px; font-weight: 400;
    letter-spacing: 1px; color: var(--navy); text-transform: uppercase;
  }
  .front-stripe { position: absolute; left: 0; bottom: 0; height: 6px; }
  .front-stripe--navy { width: 374px; background: var(--navy); }
  .front-stripe--yellow { left: 374px; right: 0; background: var(--yellow); }

  /* Back */
  .ghost-ring {
    position: absolute; left: 20px; top: 40px;
    width: 190px; height: 190px; border-radius: 50%;
    border: 16px solid var(--ghost);
  }
  .name-accent {
    position: absolute; left: 0; top: 22px; width: 14px; height: 54px;
    background: var(--yellow);
  }
  .person-name {
    position: absolute; left: 29px; top: 30px;
    font-size: 21px; font-weight: 700; color: var(--navy);
  }
  .person-title {
    position: absolute; left: 29px; top: 58px;
    font-size: 12px; color: var(--ink);
  }
  .back-mark {
    position: absolute; left: 333px; top: 31px;
    width: 78px; height: 78px; border-radius: 50%;
    border: 5px solid var(--navy);
  }
  .back-name {
    position: absolute; left: 289px; width: 170px; top: 114px;
    text-align: center; font-size: 19px; font-weight: 400;
    letter-spacing: 0.5px; color: var(--navy); text-transform: uppercase;
  }
  .contact-list {
    position: absolute; left: 29px; top: 169px; list-style: none;
    font-size: 13px; color: var(--ink);
  }
  .contact-list li { display: flex; align-items: center; height: 17.5px; }
  .contact-list svg { width: 11px; height: 11px; margin-right: 12px; fill: var(--navy); }
  .contact-list .address { margin-top: 3px; }
  .footer-bands { position: absolute; left: 0; bottom: 0; width: 486px; height: 40px; }
  .credentials {
    position: absolute; left: 247px; bottom: 11px;
    font-size: 12.5px; color: #fff; white-space: pre;
  }
</style>
</head>
<body>
<div class="canvas">

  <section class="card card--front">
    <div class="front-mark" aria-hidden="true"></div>
    <div class="front-name">Brondle Electric</div>
    <div class="front-stripe front-stripe--navy"></div>
    <div class="front-stripe front-stripe--yellow"></div>
  </section>

  <section class="card card--back">
    <div class="ghost-ring" aria-hidden="true"></div>
    <div class="name-accent"></div>
    <h1 class="person-name">Marcus Tivane</h1>
    <p class="person-title">Managing Director</p>

    <div class="back-mark" aria-hidden="true"></div>
    <div class="back-name">Brondle Electric</div>

    <ul class="contact-list">
      <li>
        <svg viewBox="0 0 12 12"><path d="M3 0h6a1 1 0 0 1 1 1v10a1 1 0 0 1-1 1H3a1 1 0 0 1-1-1V1a1 1 0 0 1 1-1zm0.8 1.5v7.5h4.4V1.5zM6 9.8a.7.7 0 1 0 0 1.4.7.7 0 0 0 0-1.4z"/></svg>
        +111 222 3333
      </li>
      <li>
        <svg viewBox="0 0 12 12"><path d="M1 3.2C1 2 3 1.5 6 1.5s5 .5 5 1.7V5H8.5V3.8h-5V5H1zM3 6h6l2 2.5V11H1V8.5zm3 1.3a1.3 1.3 0 1 0 0 2.6 1.3 1.3 0 0 0 0-2.6z"/></svg>
        www.yourwebsite.com
      </li>
      <li>
        <svg viewBox="0 0 12 12"><path d="M0 2.5h12v7H0zm1 1v.4l5 3.2 5-3.2v-.4zm0 1.6v3.4h10V5.1L6 8.2z"/></svg>
        yourname@yourwebsite.com
      </li>
      <li class="address">3790 Street No.123 Harlow Bay California 99999</li>
    </ul>

    <svg class="footer-bands" viewBox="0 0 486 40" aria-hidden="true">
      <polygon points="0,18 229,18 217,37 0,37" fill="var(--yellow)"/>
      <polygon points="222,0 486,0 486,40 198,40" fill="var(--navy)"/>
    </svg>
    <div class="credentials">Licensed &amp; Insured   |  TECL #58917</div>
  </section>

</div>
</body>
</html>
```